Video blogger website.

I'm looking to build a video blogger website I want cool, unique design. The ability to add banners on top of page. I would like to use embedded videos from sources like Flicksy etc with the ability to share on social media . If needed I can provide example sites upon request. Like / dislike button similar to Flicksy and Video View counter .10-15 pages with the availability to add more pages as site grows. I want the overall outline of the site to be original, but I want banners and all functions all to be done in WordPress. But I don't want a completely WordPress website due to certain limitations. Please no cookie cutters!!

Target Market(s)

Music, Comedy teens to adults

Build

Coding

Coded - Design and coding required

Number of Pages Required

5+ page

Colors

Designer to choose colors to be used in the design.

Requirements
Should not have
• No log in

```html
<!DOCTYPE html>
<html lang="en">
<head>
<meta charset="utf-8">
<title>Reelvine – Video Blog</title>
<link href="https://fonts.googleapis.com/css2?family=Lato:wght@400;700;900&display=swap" rel="stylesheet">
<style>
  :root{
    --orange:#f48a1c;
    --dark:#3b3b3b;
    --darker:#333333;
    --page:#efefef;
    --band:#e6e6e6;
    --white:#ffffff;
    --text:#2b2b2b;
    --muted:#8a8a8a;
    --line:#e3e3e3;
  }
  *{box-sizing:border-box;margin:0;padding:0}
  html,body{width:1200px;height:3273px;overflow:hidden}
  body{font-family:"Lato",Arial,sans-serif;color:var(--text);background:var(--page)}
  .page{position:relative;width:1200px;height:3273px;overflow:hidden;background:var(--page)}
  .abs{position:absolute}

  /* header */
  .masthead{position:absolute;left:0;top:0;width:1200px;height:694px;background:var(--dark)}
  .brand{position:absolute;display:flex;align-items:center;gap:10px;color:var(--orange);font-weight:900;font-size:27px;letter-spacing:-.3px}
  .brand-dot{width:16px;height:16px;border-radius:50%;background:var(--orange)}
  .masthead .brand{left:131px;top:28px}
  .search{position:absolute;left:334px;top:26px;width:393px;height:42px;background:var(--white);display:flex;align-items:center;padding:0 14px;font-size:11px;color:#9a9a9a;justify-content:space-between}
  .main-nav{position:absolute;left:760px;top:38px;display:flex;gap:30px}
  .main-nav a{color:var(--white);text-decoration:none;font-size:11px;font-weight:700;text-transform:uppercase}
  .player{position:absolute;left:131px;top:113px;width:938px;height:502px;box-shadow:0 10px 30px rgba(0,0,0,.35)}
  .player-screen{position:absolute;inset:0;background:
      linear-gradient(180deg,#6d7fa0 0%,#c9a04a 32%,#f3c23a 45%,#e8a123 52%,#3b5f72 62%,#6d8ea2 80%,#2d4252 100%)}
  .player-screen::before{content:"";position:absolute;left:0;right:0;top:38%;height:20%;background:linear-gradient(90deg,#1b2a22 0%,transparent 25%,transparent 70%,#1b2a22 100%);opacity:.8}
  .big-play{position:absolute;left:448px;top:212px;width:0;height:0;border-left:36px solid rgba(255,255,255,.92);border-top:21px solid transparent;border-bottom:21px solid transparent}
  .controls{position:absolute;left:0;bottom:0;width:100%;height:44px;background:rgba(20,25,35,.55);display:flex;align-items:center;padding:0 12px;gap:16px}
  .progress{flex:1;height:3px;background:rgba(255,255,255,.55)}
  .slide-arrow{position:absolute;top:335px;width:20px;height:36px}
  .video-info{position:absolute;left:131px;top:636px;width:938px;display:flex;justify-content:space-between;align-items:center;color:var(--white)}
  .video-info h1{font-size:16px;font-weight:400}
  .video-stats{display:flex;gap:20px;font-size:11px;align-items:center}
  .video-stats span{display:flex;gap:5px;align-items:center}

  /* categories band */
  .category-bar{position:absolute;left:0;top:694px;width:1200px;height:83px;background:var(--band)}
  .category-title{position:absolute;left:131px;top:26px;line-height:1}
  .category-title small{display:block;font-size:10px;font-weight:700;color:#444}
  .category-title strong{display:block;font-size:20px;color:var(--orange);font-weight:700;margin-top:3px}
  .category-list{position:absolute;left:256px;top:0;height:83px;display:flex}
  .category-list li{list-style:none;width:81.4px;border-left:1px solid #cfcfcf;display:flex;flex-direction:column;align-items:center;justify-content:center;gap:8px;font-size:9px;font-weight:700;color:#555;text-transform:uppercase}
  .category-list svg{width:16px;height:16px;fill:#555}

  /* headings */
  .section-title{position:absolute;color:var(--orange);font-size:18px;font-weight:900;text-transform:uppercase}
  .pager{position:absolute;display:flex;gap:14px}
  .pager svg{width:10px;height:12px;stroke:#444;stroke-width:2;fill:none}

  /* cards */
  .card-grid{position:absolute;left:133px;width:935px;display:grid;grid-template-columns:repeat(4,227px);column-gap:9px;row-gap:15px}
  .card{background:var(--white);box-shadow:0 1px 3px rgba(0,0,0,.08);height:247px;display:flex;flex-direction:column}
  .thumb{position:relative;height:153px;flex:none}
  .thumb::after{content:"";position:absolute;left:50%;top:50%;transform:translate(-35%,-50%);border-left:30px solid rgba(255,255,255,.9);border-top:18px solid transparent;border-bottom:18px solid transparent}
  .card-body{padding:16px 14px 0;flex:1;display:flex;flex-direction:column}
  .card-body h3{font-size:13px;font-weight:700}
  .views{font-size:10px;color:var(--muted);margin-top:4px}
  .card-meta{margin-top:auto;height:38px;border-top:1px solid var(--line);display:flex;align-items:center;justify-content:space-between;font-size:10px;color:#555}
  .share{display:flex;align-items:center;gap:6px}
  .share i{width:7px;height:7px;border-radius:50%;background:#666;display:block}
  .stats{display:flex;gap:12px}
  .stats span{display:flex;gap:4px;align-items:center}
  .stats svg{width:10px;height:10px;fill:#555}

  .popular-panel{position:absolute;left:129px;top:1501px;width:700px;height:637px;background:var(--white)}
  .popular-grid{position:absolute;left:19px;top:24px;display:grid;grid-template-columns:317px 314px;column-gap:28px;row-gap:22px}
  .popular-grid .card{height:290px;box-shadow:none}
  .popular-grid .thumb{height:168px}
  .popular-grid .card-body{padding:20px 0 0}
  .popular-grid .card-meta{border-top:none;border-bottom:1px solid var(--line)}

  .trending{position:absolute;left:838px;top:1503px;width:229px;display:flex;flex-direction:column;gap:15px}
  .trending .card{height:232px}
  .trending .thumb{height:144px}
  .trending .card-body{padding:14px 14px 0}
  .trending .card-meta{height:34px}
  .trending .thumb-only{height:146px;position:relative}

  /* footer */
  .site-footer{position:absolute;left:0;top:2906px;width:1200px;height:367px;background:var(--dark);color:var(--white)}
  .footer-title{position:absolute;top:55px;color:var(--orange);font-size:14px;font-weight:900;text-transform:uppercase}
  .post{position:absolute;left:131px;display:flex;gap:24px}
  .post .thumb{width:98px;height:70px}
  .post .thumb::after{border-left-width:22px;border-top-width:13px;border-bottom-width:13px}
  .post h4{font-size:11px;font-weight:700;margin-top:6px}
  .post .views{color:#cfcfcf;font-size:10px}
  .post .card-meta{border:none;height:auto;margin-top:10px;color:#ddd;gap:16px;justify-content:flex-start}
  .post .share i{background:#ddd}
  .post .stats svg{fill:#ddd}
  .footer-cats{position:absolute;left:556px;top:100px;list-style:none;font-size:11px;line-height:22px}
  .site-footer .brand{right:131px;top:78px}
  .about{position:absolute;right:131px;top:142px;width:310px;text-align:right;font-size:10px;line-height:16px;color:#bdbdbd}
  .social{position:absolute;right:131px;top:3148px;display:flex;gap:16px}
  .social i{width:24px;height:24px;border-radius:50%;background:var(--white);display:block}
  .copyright{position:absolute;left:0;top:3234px;width:1200px;border-top:1px solid #4a4a4a;padding-top:16px;text-align:center;font-size:10px;color:#ccc}
</style>
</head>
<body>
<div class="page">

  <header class="masthead">
    <div class="brand"><span class="brand-dot"></span>Reelvine</div>
    <div class="search"><span>Search</span>
      <svg width="12" height="12" viewBox="0 0 12 12"><circle cx="5" cy="5" r="3.8" fill="none" stroke="#333" stroke-width="1.6"/><path d="M8 8l3 3" stroke="#333" stroke-width="1.8"/></svg>
    </div>
    <nav class="main-nav"><a href="#">Home</a><a href="#">About us</a><a href="#">Videos</a><a href="#">Contact us</a></nav>

    <svg class="slide-arrow" style="left:50px" viewBox="0 0 20 36"><path d="M16 2L4 18l12 16" stroke="#8a8a8a" stroke-width="2" fill="none"/></svg>
    <svg class="slide-arrow" style="left:1130px" viewBox="0 0 20 36"><path d="M4 2l12 16L4 34" stroke="#8a8a8a" stroke-width="2" fill="none"/></svg>

    <div class="player">
      <div class="player-screen" role="img" aria-label="Featured video still: palm trees silhouetted against a golden sunset reflected in calm water"></div>
      <div class="big-play"></div>
      <div class="controls">
        <svg width="14" height="16" viewBox="0 0 14 16"><path d="M1 1l12 7-12 7z" fill="#fff"/></svg>
        <div class="progress"></div>
        <svg width="18" height="14" viewBox="0 0 18 14"><path d="M1 5h4l5-4v12l-5-4H1z" fill="#fff"/><path d="M13 4q3 3 0 6" stroke="#fff" stroke-width="1.5" fill="none"/></svg>
        <svg width="16" height="16" viewBox="0 0 16 16" fill="none" stroke="#fff" stroke-width="1.6"><path d="M1 5V1h4M11 1h4v4M15 11v4h-4M5 15H1v-4"/><rect x="4" y="4" width="8" height="8"/></svg>
      </div>
    </div>

    <div class="video-info">
      <h1>Video Heading</h1>
      <div class="video-stats">
        <span>1,052 Views</span>
        <span><svg width="11" height="11" viewBox="0 0 10 10"><path d="M0 4h2v6H0zM3 4l3-4c1 0 1 1 1 2L6 4h4l-1 6H3z" fill="#fff"/></svg>1125</span>
        <span><svg width="11" height="11" viewBox="0 0 10 10"><path d="M0 6h2V0H0zM3 6l3 4c1 0 1-1 1-2L6 6h4L9 0H3z" fill="#fff"/></svg>10</span>
      </div>
    </div>
  </header>

  <section class="category-bar">
    <div class="category-title"><small>VIDEO BY</small><strong>Categories</strong></div>
    <ul class="category-list">
      <li><svg viewBox="0 0 16 16"><path d="M8 15L2 8.5A3.6 3.6 0 018 3a3.6 3.6 0 016 5.5z"/></svg>Health</li>
      <li><svg viewBox="0 0 16 16"><circle cx="8" cy="8" r="6.5" fill="none" stroke="#555" stroke-width="1.6"/><circle cx="8" cy="8" r="2.2"/></svg>Sports</li>
      <li><svg viewBox="0 0 16 16"><path d="M4 2l10 6-10 6z"/></svg>Entertainment</li>
      <li><svg viewBox="0 0 16 16"><path d="M2 9l2-5h8l2 5v4h-2v-2H4v2H2z"/></svg>Cars</li>
      <li><svg viewBox="0 0 16 16"><circle cx="8" cy="8" r="6"/><rect x="0" y="3" width="1.5" height="10"/><rect x="14.5" y="3" width="1.5" height="10"/></svg>Food</li>
      <li><svg viewBox="0 0 16 16"><path d="M3 1h10v14H3z" fill="none" stroke="#555" stroke-width="1.6"/><path d="M5 4h6v8H5z"/></svg>Film</li>
      <li><svg viewBox="0 0 16 16"><circle cx="8" cy="3" r="2.3"/><path d="M5 6h6l-1 5H6zM6 11h4v5H6z"/></svg>Lifestyle</li>
      <li><svg viewBox="0 0 16 16"><rect x="1" y="4" width="10" height="8" rx="1"/><path d="M11 7l4-2v6l-4-2z"/></svg>Live</li>
      <li><svg viewBox="0 0 16 16"><rect x="3" y="1" width="10" height="14" rx="1"/><path d="M5 3h6M5 6h6M5 9h6" stroke="#e6e6e6"/></svg>Trailers</li>
      <li><svg viewBox="0 0 16 16"><path d="M6 2l8-1v10a2 2 0 11-1.5-2V4L7.5 4.7V13a2 2 0 11-1.5-2z"/></svg>Music</li>
    </ul>
  </section>

  <!-- Latest videos -->
  <h2 class="section-title" style="left:131px;top:824px">Latest Videos</h2>
  <div class="card-grid" style="top:877px">
    <article class="card"><div class="thumb" role="img" aria-label="Blue train crossing a green hillside viaduct" style="background:linear-gradient(160deg,#2f6b3c,#6fa04a 55%,#2b4e7c)"></div><div class="card-body"><h3>Lorem Ipsum is simply</h3><p class="views">2653 Views</p><div class="card-meta"><div class="share">Share : <i></i><i></i><i></i><i></i></div><div class="stats"><span><svg viewBox="0 0 10 10"><path d="M0 4h2v6H0zM3 4l3-4c1 0 1 1 1 2L6 4h4l-1 6H3z"/></svg>1125</span><span><svg viewBox="0 0 10 10"><path d="M0 6h2V0H0zM3 6l3 4c1 0 1-1 1-2L6 6h4L9 0H3z"/></svg>21</span></div></div></div></article>
    <article class="card"><div class="thumb" role="img" aria-label="Snowy mountain peak lit by warm sunrise" style="background:linear-gradient(170deg,#7aa7d6,#e9c9a3 45%,#9a5a3a 70%,#c9d6e6)"></div><div class="card-body"><h3>It is a long established</h3><p class="views">2653 Views</p><div class="card-meta"><div class="share">Share : <i></i><i></i><i></i><i></i></div><div class="stats"><span><svg viewBox="0 0 10 10"><path d="M0 4h2v6H0zM3 4l3-4c1 0 1 1 1 2L6 4h4l-1 6H3z"/></svg>1125</span><span><svg viewBox="0 0 10 10"><path d="M0 6h2V0H0zM3 6l3 4c1 0 1-1 1-2L6 6h4L9 0H3z"/></svg>21</span></div></div></div></article>
    <article class="card"><div class="thumb" role="img" aria-label="Flock of white birds taking flight over water" style="background:linear-gradient(160deg,#5d6a6e,#c8cfcf 50%,#7d8a8a)"></div><div class="card-body"><h3>Denouncing pleasure</h3><p class="views">2653 Views</p><div class="card-meta"><div class="share">Share : <i></i><i></i><i></i><i></i></div><div class="stats"><span><svg viewBox="0 0 10 10"><path d="M0 4h2v6H0zM3 4l3-4c1 0 1 1 1 2L6 4h4l-1 6H3z"/></svg>1125</span><span><svg viewBox="0 0 10 10"><path d="M0 6h2V0H0zM3 6l3 4c1 0 1-1 1-2L6 6h4L9 0H3z"/></svg>21</span></div></div></div></article>
    <article class="card"><div class="thumb" role="img" aria-label="Path through a tall green bamboo forest" style="background:linear-gradient(90deg,#274d1e,#7fae3f 50%,#274d1e)"></div><div class="card-body"><h3>At vero eos et</h3><p class="views">2653 Views</p><div class="card-meta"><div class="share">Share : <i></i><i></i><i></i><i></i></div><div class="stats"><span><svg viewBox="0 0 10 10"><path d="M0 4h2v6H0zM3 4l3-4c1 0 1 1 1 2L6 4h4l-1 6H3z"/></svg>1125</span><span><svg viewBox="0 0 10 10"><path d="M0 6h2V0H0zM3 6l3 4c1 0 1-1 1-2L6 6h4L9 0H3z"/></svg>21</span></div></div></div></article>
    <article class="card"><div class="thumb" role="img" aria-label="Woman among blossoms in soft warm light" style="background:linear-gradient(150deg,#d9c6a6,#a57a55 55%,#6b4a30)"></div><div class="card-body"><h3>Lorem Ipsum is simply</h3><p class="views">2653 Views</p><div class="card-meta"><div class="share">Share : <i></i><i></i><i></i><i></i></div><div class="stats"><span><svg viewBox="0 0 10 10"><path d="M0 4h2v6H0zM3 4l3-4c1 0 1 1 1 2L6 4h4l-1 6H3z"/></svg>1125</span><span><svg viewBox="0 0 10 10"><path d="M0 6h2V0H0zM3 6l3 4c1 0 1-1 1-2L6 6h4L9 0H3z"/></svg>21</span></div></div></div></article>
    <article class="card"><div class="thumb" role="img" aria-label="Fiery orange sunset over ocean waves" style="background:linear-gradient(180deg,#3a2a28,#e0701d 40%,#f6b24a 55%,#5a3a2a)"></div><div class="card-body"><h3>It is a long established</h3><p class="views">2653 Views</p><div class="card-meta"><div class="share">Share : <i></i><i></i><i></i><i></i></div><div class="stats"><span><svg viewBox="0 0 10 10"><path d="M0 4h2v6H0zM3 4l3-4c1 0 1 1 1 2L6 4h4l-1 6H3z"/></svg>1125</span><span><svg viewBox="0 0 10 10"><path d="M0 6h2V0H0zM3 6l3 4c1 0 1-1 1-2L6 6h4L9 0H3z"/></svg>21</span></div></div></div></article>
    <article class="card"><div class="thumb" role="img" aria-label="Elephant splashing water in a yellow field" style="background:linear-gradient(160deg,#a59a4a,#d8c74a 50%,#6d6a2e)"></div><div class="card-body"><h3>Denouncing pleasure</h3><p class="views">2653 Views</p><div class="card-meta"><div class="share">Share : <i></i><i></i><i></i><i></i></div><div class="stats"><span><svg viewBox="0 0 10 10"><path d="M0 4h2v6H0zM3 4l3-4c1 0 1 1 1 2L6 4h4l-1 6H3z"/></svg>1125</span><span><svg viewBox="0 0 10 10"><path d="M0 6h2V0H0zM3 6l3 4c1 0 1-1 1-2L6 6h4L9 0H3z"/></svg>21</span></div></div></div></article>
    <article class="card"><div class="thumb" role="img" aria-label="Green leaves with sparkling dew and soft bokeh" style="background:linear-gradient(150deg,#0f3a2a,#2e8a4a 50%,#123c2a)"></div><div class="card-body"><h3>At vero eos et</h3><p class="views">2653 Views</p><div class="card-meta"><div class="share">Share : <i></i><i></i><i></i><i></i></div><div class="stats"><span><svg viewBox="0 0 10 10"><path d="M0 4h2v6H0zM3 4l3-4c1 0 1 1 1 2L6 4h4l-1 6H3z"/></svg>1125</span><span><svg viewBox="0 0 10 10"><path d="M0 6h2V0H0zM3 6l3 4c1 0 1-1 1-2L6 6h4L9 0H3z"/></svg>21</span></div></div></div></article>
  </div>

  <!-- Most popular + trending -->
  <h2 class="section-title" style="left:129px;top:1456px">Most Popular Videos</h2>
  <h2 class="section-title" style="left:836px;top:1461px">Trending</h2>
  <div class="pager" style="left:1032px;top:1465px">
    <svg viewBox="0 0 10 12" style="transform:rotate(90deg)"><path d="M7 1L2 6l5 5"/></svg>
    <svg viewBox="0 0 10 12" style="transform:rotate(-90deg)"><path d="M7 1L2 6l5 5"/></svg>
  </div>

  <section class="popular-panel">
    <div class="popular-grid">
      <article class="card"><div class="thumb" role="img" aria-label="Silhouette on a rock under a purple starry sky" style="background:linear-gradient(170deg,#3a3f7a,#b57aa6 50%,#2a1f2e 80%)"></div><div class="card-body"><h3>At vero eos et accusamus et iusto</h3><p class="views">102565 Views</p><div class="card-meta"><div class="share">Share : <i></i><i></i><i></i><i></i></div><div class="stats"><span><svg viewBox="0 0 10 10"><path d="M0 4h2v6H0zM3 4l3-4c1 0 1 1 1 2L6 4h4l-1 6H3z"/></svg>1125</span><span><svg viewBox="0 0 10 10"><path d="M0 6h2V0H0zM3 6l3 4c1 0 1-1 1-2L6 6h4L9 0H3z"/></svg>21</span></div></div></div></article>
      <article class="card"><div class="thumb" role="img" aria-label="Silhouetted trees against a hazy orange sunset" style="background:linear-gradient(170deg,#2a2018,#c7792a 45%,#f0b04a 55%,#1f1810)"></div><div class="card-body"><h3>At vero eos et accusamus et iusto</h3><p class="views">102565 Views</p><div class="card-meta"><div class="share">Share : <i></i><i></i><i></i><i></i></div><div class="stats"><span><svg viewBox="0 0 10 10"><path d="M0 4h2v6H0zM3 4l3-4c1 0 1 1 1 2L6 4h4l-1 6H3z"/></svg>1125</span><span><svg viewBox="0 0 10 10"><path d="M0 6h2V0H0zM3 6l3 4c1 0 1-1 1-2L6 6h4L9 0H3z"/></svg>21</span></div></div></div></article>
      <article class="card"><div class="thumb" role="img" aria-label="Climber in red jacket reaching up over a rocky mountain range" style="background:linear-gradient(160deg,#5b7ea6,#b8c6d6 35%,#c94a2a 55%,#7a5a3a)"></div><div class="card-body"><h3>At vero eos et accusamus et iusto</h3><p class="views">102565 Views</p><div class="card-meta"><div class="share">Share : <i></i><i></i><i></i><i></i></div><div class="stats"><span><svg viewBox="0 0 10 10"><path d="M0 4h2v6H0zM3 4l3-4c1 0 1 1 1 2L6 4h4l-1 6H3z"/></svg>1125</span><span><svg viewBox="0 0 10 10"><path d="M0 6h2V0H0zM3 6l3 4c1 0 1-1 1-2L6 6h4L9 0H3z"/></svg>21</span></div></div></div></article>
      <article class="card"><div class="thumb" role="img" aria-label="Elephant walking through sunlit green grassland" style="background:linear-gradient(170deg,#e8e0a0,#8aa84a 45%,#3f5a24)"></div><div class="card-body"><h3>At vero eos et accusamus et iusto</h3><p class="views">102565 Views</p><div class="card-meta"><div class="share">Share : <i></i><i></i><i></i><i></i></div><div class="stats"><span><svg viewBox="0 0 10 10"><path d="M0 4h2v6H0zM3 4l3-4c1 0 1 1 1 2L6 4h4l-1 6H3z"/></svg>1125</span><span><svg viewBox="0 0 10 10"><path d="M0 6h2V0H0zM3 6l3 4c1 0 1-1 1-2L6 6h4L9 0H3z"/></svg>21</span></div></div></div></article>
    </div>
  </section>

  <aside class="trending">
    <article class="card"><div class="thumb" role="img" aria-label="Hummingbird hovering against a soft green background" style="background:linear-gradient(150deg,#a8c98a,#5d9a6a 50%,#c24a5a)"></div><div class="card-body"><h3>Accusamus et iusto</h3><p class="views">102565 Views</p><div class="card-meta"><div class="share">Share : <i></i><i></i><i></i><i></i></div><div class="stats"><span><svg viewBox="0 0 10 10"><path d="M0 4h2v6H0zM3 4l3-4c1 0 1 1 1 2L6 4h4l-1 6H3z"/></svg>1125</span><span><svg viewBox="0 0 10 10"><path d="M0 6h2V0H0zM3 6l3 4c1 0 1-1 1-2L6 6h4L9 0H3z"/></svg>21</span></div></div></div></article>
    <article class="card"><div class="thumb" role="img" aria-label="Young seedling sprouting from dark soil" style="background:linear-gradient(180deg,#1e2a1a,#3e7a2a 50%,#2a1e14)"></div><div class="card-body"><h3>Accusamus et iusto</h3><p class="views">102565 Views</p><div class="card-meta"><div class="share">Share : <i></i><i></i><i></i><i></i></div><div class="stats"><span><svg viewBox="0 0 10 10"><path d="M0 4h2v6H0zM3 4l3-4c1 0 1 1 1 2L6 4h4l-1 6H3z"/></svg>1125</span><span><svg viewBox="0 0 10 10"><path d="M0 6h2V0H0zM3 6l3 4c1 0 1-1 1-2L6 6h4L9 0H3z"/></svg>21</span></div></div></div></article>
    <div class="thumb thumb-only" role="img" aria-label="Forest lake with evergreen trees on the shore" style="background:linear-gradient(180deg,#9ac0d0,#3f6a3a 40%,#2f5a4a 70%,#a04a5a)"></div>
  </aside>

  <!-- Recommended -->
  <h2 class="section-title" style="left:129px;top:2196px">Recommended</h2>
  <div class="pager" style="left:1032px;top:2201px">
    <svg viewBox="0 0 10 12"><path d="M7 1L2 6l5 5"/></svg>
    <svg viewBox="0 0 10 12"><path d="M3 1l5 5-5 5"/></svg>
  </div>
  <div class="card-grid" style="top:2250px">
    <article class="card"><div class="thumb" role="img" aria-label="Layered mountain ridges under an orange sunset sky" style="background:linear-gradient(180deg,#e2742a,#f0a04a 35%,#5a5a7a 60%,#2a3046)"></div><div class="card-body"><h3>Lorem Ipsum is simply</h3><p class="views">2653 Views</p><div class="card-meta"><div class="share">Share : <i></i><i></i><i></i><i></i></div><div class="stats"><span><svg viewBox="0 0 10 10"><path d="M0 4h2v6H0zM3 4l3-4c1 0 1 1 1 2L6 4h4l-1 6H3z"/></svg>1125</span><span><svg viewBox="0 0 10 10"><path d="M0 6h2V0H0zM3 6l3 4c1 0 1-1 1-2L6 6h4L9 0H3z"/></svg>21</span></div></div></div></article>
    <article class="card"><div class="thumb" role="img" aria-label="Tiger wading through a jungle stream" style="background:linear-gradient(170deg,#2a3a22,#6a7a3a 45%,#c08a3a 60%,#2a3a2a)"></div><div class="card-body"><h3>It is a long established</h3><p class="views">2653 Views</p><div class="card-meta"><div class="share">Share : <i></i><i></i><i></i><i></i></div><div class="stats"><span><svg viewBox="0 0 10 10"><path d="M0 4h2v6H0zM3 4l3-4c1 0 1 1 1 2L6 4h4l-1 6H3z"/></svg>1125</span><span><svg viewBox="0 0 10 10"><path d="M0 6h2V0H0zM3 6l3 4c1 0 1-1 1-2L6 6h4L9 0H3z"/></svg>21</span></div></div></div></article>
    <article class="card"><div class="thumb" role="img" aria-label="Green aurora above snowy mountains" style="background:linear-gradient(180deg,#1a4a5a,#2fae8a 35%,#c8d6e0 60%,#3a4a6a)"></div><div class="card-body"><h3>Denouncing pleasure</h3><p class="views">2653 Views</p><div class="card-meta"><div class="share">Share : <i></i><i></i><i></i><i></i></div><div class="stats"><span><svg viewBox="0 0 10 10"><path d="M0 4h2v6H0zM3 4l3-4c1 0 1 1 1 2L6 4h4l-1 6H3z"/></svg>1125</span><span><svg viewBox="0 0 10 10"><path d="M0 6h2V0H0zM3 6l3 4c1 0 1-1 1-2L6 6h4L9 0H3z"/></svg>21</span></div></div></div></article>
    <article class="card"><div class="thumb" role="img" aria-label="Golden sunlight over a hazy countryside field" style="background:linear-gradient(160deg,#f0c060,#c8903a 45%,#6a5a30)"></div><div class="card-body"><h3>At vero eos et</h3><p class="views">2653 Views</p><div class="card-meta"><div class="share">Share : <i></i><i></i><i></i><i></i></div><div class="stats"><span><svg viewBox="0 0 10 10"><path d="M0 4h2v6H0zM3 4l3-4c1 0 1 1 1 2L6 4h4l-1 6H3z"/></svg>1125</span><span><svg viewBox="0 0 10 10"><path d="M0 6h2V0H0zM3 6l3 4c1 0 1-1 1-2L6 6h4L9 0H3z"/></svg>21</span></div></div></div></article>
  </div>

  <!-- Recently viewed -->
  <h2 class="section-title" style="left:129px;top:2556px">Recently Viewed</h2>
  <div class="pager" style="left:1032px;top:2561px">
    <svg viewBox="0 0 10 12"><path d="M7 1L2 6l5 5"/></svg>
    <svg viewBox="0 0 10 12"><path d="M3 1l5 5-5 5"/></svg>
  </div>
  <div class="card-grid" style="top:2610px">
    <article class="card"><div class="thumb" role="img" aria-label="Boat on a tropical river lined with palms" style="background:linear-gradient(180deg,#8ac0e0,#3a8a3a 45%,#3a7a6a)"></div><div class="card-body"><h3>Lorem Ipsum is simply</h3><p class="views">2653 Views</p><div class="card-meta"><div class="share">Share : <i></i><i></i><i></i><i></i></div><div class="stats"><span><svg viewBox="0 0 10 10"><path d="M0 4h2v6H0zM3 4l3-4c1 0 1 1 1 2L6 4h4l-1 6H3z"/></svg>1125</span><span><svg viewBox="0 0 10 10"><path d="M0 6h2V0H0zM3 6l3 4c1 0 1-1 1-2L6 6h4L9 0H3z"/></svg>21</span></div></div></div></article>
    <article class="card"><div class="thumb" role="img" aria-label="Rows of colourful wooden boats moored together" style="background:linear-gradient(120deg,#2a5aa0,#c8402a 35%,#3a8ac0 60%,#e0a02a)"></div><div class="card-body"><h3>It is a long established</h3><p class="views">2653 Views</p><div class="card-meta"><div class="share">Share : <i></i><i></i><i></i><i></i></div><div class="stats"><span><svg viewBox="0 0 10 10"><path d="M0 4h2v6H0zM3 4l3-4c1 0 1 1 1 2L6 4h4l-1 6H3z"/></svg>1125</span><span><svg viewBox="0 0 10 10"><path d="M0 6h2V0H0zM3 6l3 4c1 0 1-1 1-2L6 6h4L9 0H3z"/></svg>21</span></div></div></div></article>
    <article class="card"><div class="thumb" role="img" aria-label="Blue and yellow macaw perched on a branch" style="background:linear-gradient(150deg,#e0b060,#c08a40 40%,#2a6ab0 60%,#e0c040)"></div><div class="card-body"><h3>Denouncing pleasure</h3><p class="views">2653 Views</p><div class="card-meta"><div class="share">Share : <i></i><i></i><i></i><i></i></div><div class="stats"><span><svg viewBox="0 0 10 10"><path d="M0 4h2v6H0zM3 4l3-4c1 0 1 1 1 2L6 4h4l-1 6H3z"/></svg>1125</span><span><svg viewBox="0 0 10 10"><path d="M0 6h2V0H0zM3 6l3 4c1 0 1-1 1-2L6 6h4L9 0H3z"/></svg>21</span></div></div></div></article>
    <article class="card"><div class="thumb" role="img" aria-label="Domed sandstone monument at dusk with birds overhead" style="background:linear-gradient(180deg,#e8c8b0,#d89a80 45%,#9a5a4a 70%,#6a4a3a)"></div><div class="card-body"><h3>At vero eos et</h3><p class="views">2653 Views</p><div class="card-meta"><div class="share">Share : <i></i><i></i><i></i><i></i></div><div class="stats"><span><svg viewBox="0 0 10 10"><path d="M0 4h2v6H0zM3 4l3-4c1 0 1 1 1 2L6 4h4l-1 6H3z"/></svg>1125</span><span><svg viewBox="0 0 10 10"><path d="M0 6h2V0H0zM3 6l3 4c1 0 1-1 1-2L6 6h4L9 0H3z"/></svg>21</span></div></div></div></article>
  </div>

  <footer class="site-footer">
    <h2 class="footer-title" style="left:131px">Recent Posts</h2>
    <article class="post" style="top:101px">
      <div class="thumb" role="img" aria-label="Green landscape at sunset" style="background:linear-gradient(160deg,#2a4a3a,#4a8a6a 50%,#c8a040)"></div>
      <div><h4>It is a long established</h4><p class="views">2653 Views</p>
        <div class="card-meta"><div class="share">Share : <i></i><i></i><i></i><i></i></div><div class="stats"><span><svg viewBox="0 0 10 10"><path d="M0 4h2v6H0zM3 4l3-4c1 0 1 1 1 2L6 4h4l-1 6H3z"/></svg>1125</span><span><svg viewBox="0 0 10 10"><path d="M0 6h2V0H0zM3 6l3 4c1 0 1-1 1-2L6 6h4L9 0H3z"/></svg>21</span></div></div></div>
    </article>
    <article class="post" style="top:208px">
      <div class="thumb" role="img" aria-label="Golden field under a setting sun" style="background:linear-gradient(180deg,#f0b040,#c8802a 50%,#4a6a2a)"></div>
      <div><h4>It is a long established</h4><p class="views">2653 Views</p>
        <div class="card-meta"><div class="share">Share : <i></i><i></i><i></i><i></i></div><div class="stats"><span><svg viewBox="0 0 10 10"><path d="M0 4h2v6H0zM3 4l3-4c1 0 1 1 1 2L6 4h4l-1 6H3z"/></svg>1125</span><span><svg viewBox="0 0 10 10"><path d="M0 6h2V0H0zM3 6l3 4c1 0 1-1 1-2L6 6h4L9 0H3z"/></svg>21</span></div></div></div>
    </article>

    <h2 class="footer-title" style="left:556px">Categories</h2>
    <ul class="footer-cats">
      <li>Health</li><li>Movie</li><li>Entertainment</li><li>Trailer</li><li>LifeStyle</li><li>Food</li><li>Live</li>
    </ul>

    <div class="brand"><span class="brand-dot"></span>Reelvine</div>
    <p class="about">But I must explain to you how all this mistaken idea of denouncing pleasure and praising pain was born and I will give you a complete account of the system, and expound the actual teachings of the great explorer of the truth, the master-builder of human happiness. No one rejects, dislikes,</p>
  </footer>
  <div class="social"><i></i><i></i><i></i></div>
  <p class="copyright">Copyrights @ 2017 All Rights Reserved</p>

</div>
</body>
</html>
```